Health care finance company startup website design

This design brief is for Ledger Loom, a small start-up company dealing with an online health care (initially dental targeted with plans for medical market) financial suite of tools. My business partners and I are looking to have a website developed for our business model.

We have developed a professional logo and would like it incorporated into the site. We are open to modifications on the logo if needed to accomplish the right design.

Our concept is a clean, simple design with a professional polish and very up-to-date web presence. The functionality of the site is simple yet powerful and we would like it’s design to complement that (including anticipated css3/html5 effects for an added dimension of UI polish).

We would like to see a design mockup of the functional elements of our site as our home page. We would also be very interested to see how your design would flow into the other pages such as search for a loan, create a payment plan, make a payment, sign in, registration, contact us and learn more.

Regarding Functional Elements:

-Simplicity is king.

-The three main functions of the site are the focus. They will operate via a series of API’s to webservices on the back-end, making the front end field focused, though we hope to have it feel friendly and simple.
-Search for a loan
-Create a payment plan
-Make a payment

Other functions of the site include:

-Sign in module
-We plan to support Kindred Link, Vortal Verify and PassGate so incorporating design for those options is a plus.

-Registration module
-Two service levels clients can register for, loans only or loans & payments
-The registration process should be divided into sections with navigation back and forth until a confirmation final screen with pdf generations and remaining “to-do items” listed.
-The registration information will be saved in our database and also auto-populate fields for PDF’s that will be generated from templates.
-The registration will send a confirmation email and support PassGate, Vortal Verify and Kindred Link, so designs should take these programmatic features into account.

-Contact us
-This will emphasize digital forms of communication (email and form submitted contact request).

-Learn more
-Explanations/faqs/tutorials
-This will contain video demonstrations/screencasts of key functions of website features

Regarding Design Elements:
-We want to be “wow’d” and don’t mind a surprise that redefines what we thought we liked regarding design.
-The following examples indicate some of the color schemes we like and design elements we hope to incorporate.
-We also recognize there is no substitute for creativity and originality.

Favorite Website Design Examples:

http://www.joggingwithmarla.example/
HD backgrounds are a plus.
These colors are great.
The bright splashes of blue, red and orange combined with black in these shades.
A predominant background of whitesmoke or beige.

https://tillbrook.example/
The HD backgrounds are sharp.
The look is very clean (though it has a slight Pearfield computers imitation).
The left to right “scrolling” is preferable to vertical scrolling.
Very pleasing to the eye.

http://www.gravelpathworks.example/
Again, use of bright, vibrant HD graphics is exceptional.
The left to right scrolling navigation is slick and likely how we would like our services to flow.

http://buzzing.visitlakeshore.example/
Love the look, feel and concepts in this site’s design
Especially colors and “photography” elements.
Updates

We've seen a few common themes in various designs submitted so far and want to add a few suggestions as we enter the final week of our design contest.

We do not want any photos of healthcare professionals or close-ups of people (families or couples or individuals).  Although we are a health care company we don't want to fall into a cliche feel for our site.  Instead we would like either objects or abstract images that have depth and are high definition, spanning from edge to edge of the width of the screen. 

We prefer shades of grey for the base color scheme with highlights of bright colors.  Please refer to the examples on the brief and use those as the best guide of what we want.  Even SketchHive's color scheme is closer to what we want than some of the submissions, so please take note of the "shades of grey" with splashes of bright accent colors.

We love the horizontal navigation bar like that seen in the gravel-path works site and anticipate our final product using a similar transition between the functions of the site.

Good luck to you all.  We are still looking for that WOW factor and hoping to see something original, that breaks the traditional mold and has a feel like the examples posted.  

Industry/Entity Type

Communication

```html
<!DOCTYPE html>
<html lang="en">
<head>
<meta charset="utf-8">
<title>Ledger Loom</title>
<link rel="stylesheet" href="https://fonts.googleapis.com/css2?family=Questrial&family=Arimo:ital,wght@0,400;0,700;1,700&display=swap">
<style>
:root{
  --leaf:#8fd13a;
  --leaf-soft:#d9f0b8;
  --mint:#cfeee0;
  --sky:#1a8fc0;
  --panel:rgba(255,255,255,.86);
  --bar:#646464;
  --active:#6fb52c;
  --login:rgba(104,178,40,.9);
  --field:#e6f3da;
  --ink:#4a4a4a;
  --ink-dark:#222;
  --black:#0b0b0b;
  --orange:#f7a800;
  --white:#fff;
}
*{box-sizing:border-box;margin:0;padding:0}
html,body{width:1200px;height:1080px;overflow:hidden}
body{position:relative;font-family:"Questrial",sans-serif;color:var(--ink)}
.backdrop{position:absolute;inset:0;
  background:
    radial-gradient(ellipse 520px 420px at 930px 640px,rgba(150,215,60,.9),transparent 70%),
    radial-gradient(ellipse 600px 500px at 1150px 200px,rgba(160,220,70,.8),transparent 70%),
    radial-gradient(ellipse 500px 400px at 150px 120px,rgba(190,235,225,.9),transparent 70%),
    linear-gradient(120deg,#c9ecd8 0%,#e4f4d0 45%,#b9e27a 80%,#8fcf3b 100%);}
.abs{position:absolute}

.brand-tab{left:36px;top:0;width:422px;height:103px;border-radius:0 0 8px 8px;
  background:linear-gradient(#e4ecde,#b7c3ad);box-shadow:0 2px 4px rgba(0,0,0,.3);
  display:flex;align-items:center;padding-left:30px;gap:18px}
.brand-mark{width:62px;height:62px;border-radius:8px;background:#2a3040;flex:none}
.brand-name{font-size:44px;color:#3c3c3c;letter-spacing:.5px;white-space:nowrap}

.signin-tab{left:1099px;top:2px;width:95px;height:36px;background:#f3f3ef;border-radius:6px 6px 0 0;
  font-size:20px;color:#333;text-align:center;line-height:38px;box-shadow:0 -1px 2px rgba(0,0,0,.15)}
.signin{left:925px;top:34px;width:269px;height:254px;background:#f3f3ef;border-radius:6px 0 6px 6px;
  box-shadow:0 1px 3px rgba(0,0,0,.25);padding:26px 14px}
.signin .field{height:38px;background:var(--white);border:1px solid #ddd;border-radius:4px;
  font-family:"Arimo",sans-serif;font-size:13px;color:#666;line-height:36px;padding-left:38px;margin-bottom:15px;position:relative}
.signin .field::before{content:"";position:absolute;left:14px;top:14px;width:13px;height:9px;background:#c8c8c8;border-radius:1px}
.signin .row{display:flex;justify-content:space-between;align-items:center;margin-top:2px}
.forgot{font-family:"Arimo",sans-serif;font-size:13px;color:#2a9bd6;text-decoration:underline}
.signup{background:var(--orange);font-family:"Arimo",sans-serif;font-size:12px;color:#222;padding:3px 8px;border-radius:3px}
.or{margin:28px 0 12px;border-top:1px solid #999;text-align:center;height:1px}
.or span{position:relative;top:-8px;background:#f3f3ef;padding:0 4px;font-size:11px;color:#444;font-family:"Arimo",sans-serif}
.kindred{height:36px;background:linear-gradient(#5b79b8,#3b5998);border:1px solid #2c4479;color:var(--white);
  font-family:"Arimo",sans-serif;font-weight:700;font-size:15px;line-height:34px;padding-left:10px;
  display:flex;gap:10px;align-items:center;white-space:nowrap;overflow:hidden}
.kindred i{width:22px;height:22px;background:#fff;opacity:.25;display:block;flex:none}

.welcome{left:60px;top:127px;width:515px;height:466px;background:var(--panel);border-radius:8px;padding:15px 16px}
.welcome h1{font-weight:400;font-size:29px;color:var(--sky)}
.welcome h2{font-weight:400;font-size:23px;color:#333;text-decoration:underline;text-underline-offset:4px;margin:18px 0 26px}
.welcome p{font-family:"Arimo",sans-serif;font-size:12.4px;line-height:21.6px;color:#555;margin-bottom:21px}
.bubble{left:344px;top:520px;width:118px;height:90px;border-radius:50%;background:rgba(255,255,255,.92)}
.bubble-small{left:364px;top:612px;width:38px;height:28px;border-radius:50%;background:var(--white)}

.nav{left:37px;top:628px;width:1126px;height:117px;background:var(--bar);border-radius:10px}
.nav-item{position:absolute;top:0;height:117px;width:170px;text-align:center;color:var(--white);font-size:17px;line-height:21px}
.nav-item .icon{width:44px;height:46px;margin:14px auto 10px;border-radius:50%;background:rgba(255,255,255,.25)}
.nav-item.active{background:var(--active);top:-6px;height:130px;width:135px;left:241px}
.nav-item .label{display:block}
.q{font-size:48px;line-height:60px;color:#222;margin-top:6px;font-family:"Arimo",sans-serif;font-weight:700}

.client{left:40px;top:763px;width:324px;height:294px;background:var(--login);border-radius:5px;padding:16px 18px;color:var(--white)}
.client h3{font-weight:400;font-size:22px;margin-bottom:24px}
.client .line{display:flex;align-items:center;margin-bottom:20px}
.client label{width:89px;font-family:"Arimo",sans-serif;font-weight:700;font-style:italic;font-size:14px}
.client .input{width:199px;height:35px;background:var(--field);border-radius:8px}
.vortal{margin:0 0 0 33px;width:255px;height:46px;background:linear-gradient(#4c9320,#2f6b12);border-radius:3px;
  display:flex;align-items:center;gap:12px;padding-left:16px;font-family:"Arimo",sans-serif;font-size:16px;white-space:nowrap}
.vortal i{width:32px;height:32px;background:#fff;border-radius:3px;display:block;flex:none}
.login-btn{margin:19px 0 0 163px;width:125px;height:25px;background:linear-gradient(#777,#111);border:1px solid #ddd;border-radius:6px;
  font-family:"Arimo",sans-serif;font-weight:700;font-style:italic;font-size:14px;text-align:center;line-height:23px}

.contact{left:916px;top:764px;width:259px;height:210px;background:var(--black);border-radius:6px 6px 0 0;padding:8px 10px}
.contact h3{font-weight:400;font-size:24px;color:var(--white);margin:0 0 8px 12px}
.contact .input{background:var(--white);border-radius:3px;height:27px;margin-bottom:7px;font-family:"Arimo",sans-serif;font-size:13px;color:#777;padding:5px 9px}
.contact .message{height:65px}
.submit{margin:11px 0 0 139px;width:103px;height:25px;background:var(--orange);font-size:18px;text-align:center;line-height:25px;color:#111}

.footer{left:379px;top:971px;width:796px;height:109px;background:var(--black);color:var(--white);padding:16px 18px}
.foot-brand{display:flex;align-items:center;gap:14px}
.foot-brand .brand-mark{width:46px;height:46px;background:#666}
.foot-brand .brand-name{font-size:32px;color:#9a9a9a}
.foot-links{font-size:13px;margin-top:8px;line-height:21px}
.follow{position:absolute;left:478px;top:24px;font-size:13px;display:flex;align-items:center}
.accept{position:absolute;left:478px;top:66px;font-size:13px;display:flex;align-items:center}
.follow .sep,.accept .sep{margin:0 18px 0 24px}
.social{display:flex;gap:14px;margin-left:44px}
.social i{width:28px;height:28px;border-radius:4px;display:block}
.cards{display:flex;gap:11px}
.cards i{width:31px;height:19px;border-radius:2px;background:#e6e6e6;display:block}
</style>
</head>
<body>
<div class="backdrop" role="img" aria-label="Soft high definition abstract background of green and mint light streaks"></div>

<header class="abs brand-tab">
  <span class="brand-mark"></span>
  <span class="brand-name">LEDGER LOOM</span>
</header>

<div class="abs signin-tab">Sign in</div>
<section class="abs signin">
  <div class="field">Email</div>
  <div class="field">Password</div>
  <div class="row"><span class="forgot">Forgot password?</span><span class="signup">Sign up</span></div>
  <div class="or"><span>( or )</span></div>
  <div class="kindred"><i></i>Login with Kindred Link</div>
</section>

<section class="abs welcome">
  <h1>Welcome to Ledger Loom</h1>
  <h2>Search for a loan</h2>
  <p>Duis autem vel eum iriure dolor in hendrerit in vulputate velit esse molestie consequat, vel illum dolore eu feugiat nulla facilisis at vero eros et accumsan et iusto odio dignissim qui blandit praesent luptatum zzril delenit augue duis dolore te feugait nulla facilisi. Nam liber tempor cum soluta nobis eleifend option congue nihil imperdiet doming id quod mazim placerat facer possim assum.</p>
  <p>Typi non habent claritatem insitam; est usus legentis in iis qui facit eorum claritatem. Investigationes demonstraverunt lectores legere me lius quod ii legunt saepius. Claritas est etiam processus dynamicus, qui sequitur mutationem consuetudium lectorum. Mirum est notare quam littera gothica, quam nunc putamus parum claram, anteposuerit litterarum formas humanitatis per seacula quarta decima et quinta decima. Eodem modo typi, qui nunc nobis videntur parum clari, fiant sollemnes in futurum.</p>
</section>
<div class="abs bubble"></div>

<nav class="abs nav">
  <div class="nav-item" style="left:72px">
    <div class="icon" role="img" aria-label="Icon of a business person"></div>
    <span class="label">Who We are ?</span>
  </div>
  <div class="nav-item active">
    <svg width="44" height="46" viewBox="0 0 44 46" style="margin:16px auto 8px;display:block">
      <circle cx="17" cy="17" r="11" fill="none" stroke="#1d3d0a" stroke-width="6"/>
      <line x1="25" y1="25" x2="36" y2="38" stroke="#1d3d0a" stroke-width="8" stroke-linecap="round"/>
    </svg>
    <span class="label">Search for<br>a Loan</span>
  </div>
  <div class="nav-item" style="left:453px">
    <div class="icon" role="img" aria-label="Icon of banknotes and a calculator"></div>
    <span class="label">Create a<br>payment plan</span>
  </div>
  <div class="nav-item" style="left:676px">
    <div class="icon" role="img" aria-label="Icon of a money bag and coins"></div>
    <span class="label">Make a<br>payment</span>
  </div>
  <div class="nav-item" style="left:876px">
    <div class="q">?</div>
    <span class="label">FAQ</span>
  </div>
</nav>
<div class="abs bubble-small"></div>

<section class="abs client">
  <h3>Client Login</h3>
  <div class="line"><label>Name</label><span class="input"></span></div>
  <div class="line"><label>Password</label><span class="input"></span></div>
  <div class="vortal"><i></i>Connect with Vortal Verify</div>
  <div class="login-btn">Login</div>
</section>

<section class="abs contact">
  <h3>Quick Contact</h3>
  <div class="input">Name</div>
  <div class="input">Email Id</div>
  <div class="input message">Message</div>
  <div class="submit">Submit</div>
</section>

<footer class="abs footer">
  <div class="foot-brand"><span class="brand-mark"></span><span class="brand-name">LEDGER LOOM</span></div>
  <div class="foot-links">privacy policy - terms and conditions - user agreement<br>© 2012 Ledger Loom. All rights reserved.</div>
  <div class="follow">Follow us<span class="sep">:</span>
    <div class="social">
      <i style="background:#3b5998"></i><i style="background:#33ccff"></i><i style="background:#e2e2e2"></i><i style="background:#f39200"></i>
    </div>
  </div>
  <div class="accept">We Accept<span class="sep">:</span>
    <div class="cards"><i></i><i></i><i></i><i></i><i></i></div>
  </div>
</footer>
</body>
</html>
```